Signage for Multi-family Veterans Housing community

Need a design concept package for the above. Need Historic feel design logo element together with "Ashcombe Veterans Village"in serif font, for a Veterans (retired military) Affordable Housing community, in the historic town of Windsor, California USA. I have attached an architectural drawing of the future housing community, that will need the signage. Also, attached are photos of the town of Windsor signage, for the historic downtown vibe, do not use the sign elements. Please include in the concept package a community ID sign similar to the craftsman community ID sign attached. The community ID sign will have the logo with name and address only, use a placeholder for Address. Thank you

Font styles to use
Serif
Sans Serif

Requirements
Should not have
• Please no American flags or other military references. Other than the word “I Veterans” in the title.

```html
<!DOCTYPE html>
<html lang="en">
<head>
<meta charset="utf-8">
<title>Ashcombe Veterans Village – Community ID Sign</title>
<link rel="stylesheet" href="https://fonts.googleapis.com/css2?family=Playfair+Display:wght@700;800;900&family=Montserrat:wght@500;600&display=swap">
<style>
  :root {
    --page-dark: #3b3b3b;
    --page-light: #8c8c8c;
    --frame: #2f0d0e;
    --wood-deep: #5a1e10;
    --wood-mid: #7a2e16;
    --wood-warm: #93401c;
    --ink-white: #ffffff;
    --accent-red: #9b1c1c;
  }
  html, body {
    margin: 0;
    width: 900px;
    height: 1200px;
    overflow: hidden;
  }
  body {
    background: linear-gradient(90deg, var(--page-dark) 0%, #5c5c5c 55%, var(--page-light) 100%);
    display: flex;
    align-items: center;
    justify-content: center;
  }
  .community-sign {
    width: 840px;
    height: auto;
    filter: drop-shadow(10px 14px 22px rgba(0,0,0,0.45));
  }
  .sign-name {
    font-family: "Playfair Display", Georgia, serif;
    font-weight: 900;
    font-size: 124px;
    fill: var(--ink-white);
  }
  .sign-subtitle {
    font-family: "Playfair Display", Georgia, serif;
    font-weight: 700;
    font-size: 66px;
    fill: var(--ink-white);
  }
  .sign-band-text {
    font-family: "Montserrat", Arial, sans-serif;
    font-weight: 600;
    font-size: 29px;
    fill: var(--accent-red);
  }
  .sign-tagline {
    font-family: "Playfair Display", Georgia, serif;
    font-weight: 800;
    font-size: 33px;
    fill: var(--ink-white);
    letter-spacing: 0.5px;
  }
  .sign-location {
    font-family: "Montserrat", Arial, sans-serif;
    font-weight: 500;
    font-size: 37px;
    fill: var(--ink-white);
  }
</style>
</head>
<body>
  <svg class="community-sign" viewBox="0 0 1060 740" xmlns="http://www.w3.org/2000/svg" aria-label="Ashcombe Veterans Village community ID sign">
    <defs>
      <linearGradient id="woodGrain" x1="0" y1="0" x2="1" y2="0">
        <stop offset="0" stop-color="var(--wood-deep)"/>
        <stop offset="0.2" stop-color="var(--wood-mid)"/>
        <stop offset="0.45" stop-color="var(--wood-warm)"/>
        <stop offset="0.7" stop-color="var(--wood-mid)"/>
        <stop offset="1" stop-color="var(--wood-deep)"/>
      </linearGradient>
    </defs>

    <!-- outer frame -->
    <path class="sign-frame" fill="var(--frame)"
          d="M0,132 H280 C330,60 420,0 530,0 C640,0 730,60 780,132 H1060 V736 H0 Z"/>

    <!-- wood panel -->
    <path class="sign-panel" fill="url(#woodGrain)" role="img" aria-label="Dark walnut wood grain panel"
          d="M28,160 H294 C342,94 430,28 530,28 C630,28 718,94 766,160 H1032 V708 H28 Z"/>
    <path class="sign-inline" fill="none" stroke="var(--ink-white)" stroke-width="3"
          d="M30,162 H295 C343,96 431,30 530,30 C629,30 717,96 765,162 H1030 V706 H30 Z"/>

    <!-- top flourish placeholder -->
    <rect class="sign-flourish" role="img" aria-label="Decorative scroll flourish"
          x="425" y="95" width="210" height="58" rx="29" fill="var(--ink-white)" opacity="0.18"/>

    <text class="sign-name" x="530" y="310" text-anchor="middle" textLength="680" lengthAdjust="spacing">Ashcombe</text>
    <text class="sign-subtitle" x="530" y="388" text-anchor="middle" textLength="652" lengthAdjust="spacingAndGlyphs">VETERANS VILLAGE</text>

    <!-- laurel placeholder -->
    <rect class="sign-laurel" role="img" aria-label="Decorative laurel sprigs"
          x="372" y="412" width="316" height="36" rx="18" fill="var(--ink-white)" opacity="0.18"/>

    <rect class="sign-band" x="123" y="488" width="814" height="47" fill="var(--ink-white)"/>
    <text class="sign-band-text" x="530" y="522" text-anchor="middle">FOR A VETERANS (RETIRED MILITARY)</text>

    <text class="sign-tagline" x="530" y="577" text-anchor="middle">Affordable Housing Community</text>

    <!-- divider -->
    <g class="sign-divider" stroke="var(--ink-white)" fill="none" stroke-width="2">
      <line x1="452" y1="606" x2="608" y2="606"/>
      <path d="M442,600 L448,606 L442,612"/>
      <path d="M618,600 L612,606 L618,612"/>
    </g>
    <g fill="var(--ink-white)">
      <circle cx="524" cy="613" r="1.5"/><circle cx="530" cy="613" r="1.5"/><circle cx="536" cy="613" r="1.5"/>
    </g>

    <text class="sign-location" x="530" y="668" text-anchor="middle">Historic town of Windsor, California USA</text>
  </svg>
</body>
</html>
```